Photography and Political Commentary Blog

Hi there!
I'd like to build a clean, simple, yet visually appealing blog using a theme similar to this: http://www.brightlayouts.net/demo/?theme=TheFrame. I’m looking to work with a designer who has a modern aesthetic who can work with me to create a great blog. Hopefully that’s you!
Details:
The aim would be for the blog to be simple and clean, with each post represented by a picture, title and short summary as with ‘The Frame’ theme. These post summaries would be displayed in a single area without sidebars or columns.
There would be a home page in addition to four pages that you can access from a menu panel. These subordinate pages would be very similar if not the same in style to the main page. The subordinate pages would be:
- Politics
- Security
- Photography
- Music
For each page:
Politics and Security. These pages would be in a traditional blog format with the ability to post, hyperlink, comment etc. Posts would typically be 200-400 words. I am in the military and actively involved in politics and would like to be able to post my thoughts on issues ‘Quick Thoughts on Big Ideas’, and hyperlink to articles with short personal comments.
Photography. The photography main page would be like the homepage with each post represented by a single photo, title and summary (as per ‘The Frame’ theme). The individual posts would need to be able to display photo galleries in a grid, with the ability to click on individual photos to view them in high definition. I am open to the use of different widgets to best display the photos. Typically, each gallery would have 6-10 photos. I am a keen amateur (semi-professional?) photographer. This page would showcase small galleries of my artistic work as opposed to large journal/travel style galleries.
Music. This page is a simply way for me to post links to songs I like from ClipNest, Reelo, Tunebarn etc.
I like the clean style and typeface of the following blogs:
http://www.gallowmark.com/
http://www.thecusp.com/
http://quenlatori.com/
http://hollyonstuffs.com/
http://whatmysisterpicked.jotpage.com/
I like color palates similar to these –
http://www.huevault.com/palette/482137/Moss_Heron
http://www.huevault.com/palette/2958/Cedar_Nine
The first file I have attached is a logo that uses the types of colors and look I'd like to achieve. The second file I have attached has the type of font I'd like to use (something in the 'Sans' family: http://www.typecrate.com/fonts/category/sans/
In general, I like the use of red highlights with other neutral tones (greys, blues etc) but I’m open to your ideas!
For the function of the blog, the homepage would be a sequential summary of the posts from each of the subsections (politics, security, photography and music). I'd like this to be grouped so you can see 3 or 4 of the most recent posts from each section - but I'm open to ideas. The main pages for each subsection would be the same: a sequential summary of the posts for that area. If using Wordpress, I would like to be able to do this automatically, for instance by allocating ‘categories’ to each post that sort the posts into their respective sections.
The site name will be gavinmarsh.com.au. Any logos or headings would be my name ‘Gavin Marsh’. I already own the domain name.
The main aim for this project is for it to be clean, simple and elegant (in a modern way). Something that people can open and easily navigate without clutter, yet is visually appealing.
Thanks for taking the time to read this brief and really looking forward to working with you!
Cheers!
Gav

```html
<!DOCTYPE html>
<html lang="en">
<head>
<meta charset="utf-8">
<title>Gavin Marsh — Photography &amp; Politics</title>
<link href="https://fonts.googleapis.com/css2?family=Source+Sans+3:wght@400;600&family=Oswald:wght@300&display=swap" rel="stylesheet">
<style>
  :root {
    --page-bg: #3a475c;
    --bar-bg: #2d3648;
    --footer-bg: #2b3444;
    --accent: #e0503c;
    --accent-dark: #c5402f;
    --sage: #8fa89d;
    --rule: #8a9f96;
    --text-light: #e8ecef;
    --text-muted: #b7c0ca;
    --nav-text: #dfe4ea;
  }
  * { box-sizing: border-box; margin: 0; padding: 0; }
  html, body { width: 1200px; height: 2177px; overflow: hidden; }
  body {
    background: var(--page-bg);
    font-family: "Source Sans 3", "Myriad Pro", sans-serif;
    color: var(--text-light);
    position: relative;
  }
  a { color: inherit; text-decoration: none; }

  /* Top bar */
  .site-header { position: absolute; top: 0; left: 0; width: 1200px; height: 83px; background: var(--bar-bg); }
  .brand {
    position: absolute; left: 0; top: 0; width: 440px; height: 83px; background: var(--accent);
    display: flex; align-items: center; justify-content: center;
    font-size: 19px; letter-spacing: 4px; color: #fff; font-weight: 400;
  }
  .main-nav a { position: absolute; top: 34px; font-size: 13px; color: var(--nav-text); }

  /* Intro columns */
  .intro { position: absolute; top: 120px; left: 173px; width: 857px; display: flex; gap: 34px; }
  .intro-item { width: 263px; height: 120px; border-bottom: 4px solid var(--rule); }
  .intro-item h2 { font-size: 16px; font-weight: 400; letter-spacing: 1.5px; color: var(--sage); margin-bottom: 14px; }
  .intro-item p { font-size: 10.5px; line-height: 21px; color: var(--text-muted); }

  /* Banner */
  .hero {
    position: absolute; top: 268px; left: 173px; width: 857px; height: 233px; background: var(--accent);
  }
  .hero-title {
    position: absolute; left: 44px; top: 103px;
    font-family: "Oswald", "Arial Narrow", sans-serif; font-weight: 300;
    font-size: 31px; line-height: 50px; letter-spacing: 5px; color: #fff;
  }
  .hero-arrows { position: absolute; right: 9px; bottom: 8px; display: flex; gap: 2px; }
  .hero-arrows span { width: 30px; height: 18px; background: var(--accent-dark); display: flex; align-items: center; justify-content: center; }

  /* Portfolio */
  .section-title {
    position: absolute; top: 545px; left: 0; width: 1200px; text-align: center;
    font-size: 14px; letter-spacing: 2px; color: var(--text-muted); font-weight: 400;
  }
  .portfolio {
    position: absolute; top: 598px; left: 173px; width: 858px;
    display: grid; grid-template-columns: repeat(3, 286px); grid-auto-rows: 364px;
  }
  .post-card { text-align: center; }
  .post-photo { width: 286px; height: 197px; }
  .post-body { height: 167px; padding-top: 24px; }
  .post-card.is-active .post-body { background: var(--accent); }
  .post-title { font-size: 14.5px; font-weight: 400; letter-spacing: 1.5px; color: var(--sage); }
  .post-card.is-active .post-title { color: #fff; font-weight: 600; }
  .post-meta { font-size: 10px; letter-spacing: 1.5px; color: var(--text-muted); margin-top: 6px; }
  .post-card.is-active .post-meta { color: #fff; }
  .post-excerpt { font-size: 11px; line-height: 21.5px; letter-spacing: 1px; color: var(--text-light); margin: 9px auto 0; width: 225px; }

  /* Footer */
  .site-footer { position: absolute; left: 0; top: 2079px; width: 1200px; height: 98px; background: var(--footer-bg); }
  .footer-nav a { position: absolute; top: 22px; font-size: 10.5px; letter-spacing: 1.5px; color: var(--text-muted); }
  .copyright { position: absolute; left: 173px; top: 55px; font-size: 10.5px; letter-spacing: 1.5px; color: var(--text-muted); }
  .social-links { position: absolute; left: 745px; top: 44px; display: flex; gap: 14px; font-size: 10px; letter-spacing: 0.5px; color: var(--text-muted); }
</style>
</head>
<body>
  <header class="site-header">
    <a class="brand" href="#">Gavin Marsh</a>
    <nav class="main-nav">
      <a href="#" style="left:491px">Home</a>
      <a href="#" style="left:593px">About Us</a>
      <a href="#" style="left:712px">Politics</a>
      <a href="#" style="left:819px">Photography</a>
      <a href="#" style="left:958px">News</a>
    </nav>
  </header>

  <section class="intro">
    <article class="intro-item">
      <h2>About Gavin Marsh</h2>
      <p>It is a long established fact that a reader will be distracted by the readable content of a page when looking at its layout content...</p>
    </article>
    <article class="intro-item">
      <h2>Photography</h2>
      <p>It is a long established fact that a reader will be distracted by the readable content of a page when looking at its layout content...</p>
    </article>
    <article class="intro-item">
      <h2>Politics</h2>
      <p>It is a long established fact that a reader will be distracted by the readable content of a page when looking at its layout content...</p>
    </article>
  </section>

  <section class="hero">
    <p class="hero-title">Its a blog about<br>photography and political news discussions.</p>
    <div class="hero-arrows">
      <span><svg width="14" height="8" viewBox="0 0 14 8"><path d="M13 4H1M4 1L1 4l3 3" fill="none" stroke="#f2a397" stroke-width="1"/></svg></span>
      <span><svg width="14" height="8" viewBox="0 0 14 8"><path d="M1 4h12M10 1l3 3-3 3" fill="none" stroke="#f2a397" stroke-width="1"/></svg></span>
    </div>
  </section>

  <h2 class="section-title">Portfolio</h2>

  <section class="portfolio">
    <article class="post-card is-active">
      <div class="post-photo" role="img" aria-label="Black and white photo of a speaker gesturing in the rain" style="background:linear-gradient(135deg,#2a2a2a,#6b6b6b 55%,#1d1d1d)"></div>
      <div class="post-body"><h3 class="post-title">At Home With Rosa Wendell</h3><p class="post-meta">14 Dec 2013 / 1,202 notes</p><p class="post-excerpt">It is a long established fact that a reader will be distracted by the readable content...</p></div>
    </article>
    <article class="post-card">
      <div class="post-photo" role="img" aria-label="Vintage red car parked on a sunny city street" style="background:linear-gradient(160deg,#d8cf9a,#a58e5a 45%,#b23a32 75%,#3e3429)"></div>
      <div class="post-body"><h3 class="post-title">At Home With Rosa Wendell</h3><p class="post-meta">14 Dec 2013 / 1,202 notes</p><p class="post-excerpt">It is a long established fact that a reader will be distracted by the readable content...</p></div>
    </article>
    <article class="post-card">
      <div class="post-photo" role="img" aria-label="Dancer in a flowing white dress on a city rooftop" style="background:linear-gradient(170deg,#cbc4b6,#8d8474 50%,#3a3128)"></div>
      <div class="post-body"><h3 class="post-title">At Home With Rosa Wendell</h3><p class="post-meta">14 Dec 2013 / 1,202 notes</p><p class="post-excerpt">It is a long established fact that a reader will be distracted by the readable content...</p></div>
    </article>

    <article class="post-card">
      <div class="post-photo" role="img" aria-label="Photographer lying on a pebble beach next to a seal" style="background:linear-gradient(150deg,#7f8c96,#5f6b55 50%,#8c8f8e)"></div>
      <div class="post-body"><h3 class="post-title">At Home With Rosa Wendell</h3><p class="post-meta">14 Dec 2013 / 1,202 notes</p><p class="post-excerpt">It is a long established fact that a reader will be distracted by the readable content...</p></div>
    </article>
    <article class="post-card">
      <div class="post-photo" role="img" aria-label="Faded purple-toned view of a canal with a spire" style="background:linear-gradient(180deg,#c8c3a8,#7a5a74 55%,#4a2f52)"></div>
      <div class="post-body"><h3 class="post-title">At Home With Rosa Wendell</h3><p class="post-meta">14 Dec 2013 / 1,202 notes</p><p class="post-excerpt">It is a long established fact that a reader will be distracted by the readable content...</p></div>
    </article>
    <article class="post-card">
      <div class="post-photo" role="img" aria-label="Aerial view of a crowd reaching hands into a circle" style="background:radial-gradient(circle at 50% 45%,#3a2818,#b05a1e 45%,#d38a3a 75%,#6e3a18)"></div>
      <div class="post-body"><h3 class="post-title">At Home With Rosa Wendell</h3><p class="post-meta">14 Dec 2013 / 1,202 notes</p><p class="post-excerpt">It is a long established fact that a reader will be distracted by the readable content...</p></div>
    </article>

    <article class="post-card">
      <div class="post-photo" role="img" aria-label="Soldiers leading people through rubble beside a fire" style="background:linear-gradient(120deg,#8c5a2a,#5a5040 40%,#756a5c 70%,#3c3a34)"></div>
      <div class="post-body"><h3 class="post-title">At Home With Rosa Wendell</h3><p class="post-meta">14 Dec 2013 / 1,202 notes</p><p class="post-excerpt">It is a long established fact that a reader will be distracted by the readable content...</p></div>
    </article>
    <article class="post-card">
      <div class="post-photo" role="img" aria-label="Black and white photo of press photographers in a crowd" style="background:linear-gradient(140deg,#d4d4d4,#6a6a6a 50%,#2c2c2c)"></div>
      <div class="post-body"><h3 class="post-title">At Home With Rosa Wendell</h3><p class="post-meta">14 Dec 2013 / 1,202 notes</p><p class="post-excerpt">It is a long established fact that a reader will be distracted by the readable content...</p></div>
    </article>
    <article class="post-card">
      <div class="post-photo" role="img" aria-label="Dark portrait of an elderly woman with long dreadlocks" style="background:radial-gradient(circle at 60% 45%,#7a5a3e,#3a2a1e 55%,#120d0a)"></div>
      <div class="post-body"><h3 class="post-title">At Home With Rosa Wendell</h3><p class="post-meta">14 Dec 2013 / 1,202 notes</p><p class="post-excerpt">It is a long established fact that a reader will be distracted by the readable content...</p></div>
    </article>

    <article class="post-card">
      <div class="post-photo" role="img" aria-label="Sepia portrait of a politician looking upward" style="background:linear-gradient(135deg,#e6e2dc,#8a8078 50%,#3a3430)"></div>
      <div class="post-body"><h3 class="post-title">At Home With Rosa Wendell</h3><p class="post-meta">14 Dec 2013 / 1,202 notes</p><p class="post-excerpt">It is a long established fact that a reader will be distracted by the readable content...</p></div>
    </article>
    <article class="post-card">
      <div class="post-photo" role="img" aria-label="Crowd with cameras in front of a city skyline" style="background:linear-gradient(180deg,#9fc0e0,#b8c8d2 40%,#5a4a3c 70%,#2e2620)"></div>
      <div class="post-body"><h3 class="post-title">At Home With Rosa Wendell</h3><p class="post-meta">14 Dec 2013 / 1,202 notes</p><p class="post-excerpt">It is a long established fact that a reader will be distracted by the readable content...</p></div>
    </article>
    <article class="post-card">
      <div class="post-photo" role="img" aria-label="Black and white conference room with a round table and screens" style="background:linear-gradient(180deg,#8a8a8a,#2a2a2a 45%,#111)"></div>
      <div class="post-body"><h3 class="post-title">At Home With Rosa Wendell</h3><p class="post-meta">14 Dec 2013 / 1,202 notes</p><p class="post-excerpt">It is a long established fact that a reader will be distracted by the readable content...</p></div>
    </article>
  </section>

  <footer class="site-footer">
    <nav class="footer-nav">
      <a href="#" style="left:173px">Home</a>
      <a href="#" style="left:259px">About Us</a>
      <a href="#" style="left:364px">Politics</a>
      <a href="#" style="left:460px">Photography</a>
      <a href="#" style="left:587px">News</a>
    </nav>
    <p class="copyright">©2013. Gavin Marsh. All rights reserved.</p>
    <nav class="social-links">
      <a href="#">Linkbook</a>
      <a href="#">Chirper</a>
      <a href="#">Circlet</a>
      <a href="#">Pinwall</a>
      <a href="#">Worklink</a>
      <a href="#">ClipNest</a>
      <a href="#">Feed</a>
    </nav>
  </footer>
</body>
</html>
```